Wrenfield Inc. Website & Zulmax Apps Landing Pages

We need a web site design for our company. We develop software and do various consultant projects for our clients. Our products focus on the mobile platform, mainly the Zulmax (business, games, social, etc.). We want to communicate that our software is simple and good as candy. The web pages should be fun to look at not loosing seriousness and credibility. Web 2.0 style and 960 grid system a must. We are opened to any overall site colour scheme suggestions (look at the sites we like below).

Must haves:
- Our logo should be seen on the site and look great on it :-) (preview attached below)
- Main home page and app landing page.
- Section links/tabs on the home page (home,apps,support,blog,contact,about)
- No text in images
- Style sheet

Looks we like:
- http://x7k3pq9wrt4mvb.imgvault-demo.net/412_Kelto_Site/final_large.jpg
- http://x7k3pq9wrt4mvb.imgvault-demo.net/Premium_71_Illustrative_Zulmax_Landing_Page/final.jpg
- http://gravelnook.com/
- http://lumfray.ca/
- http://pinecask.com/

Industry/Entity Type

Business

Requirements
Must have
• - Company logo should look great on pages.
• - Main home page and app landing page.
• - Section links/tabs on the home page (home,apps,support,blog,contact,about)
• - Web 2.0 style.
• - 960 grid system (12 col, 16 col).
• - Sliced ann optmized
• - Exported in all major formats (psd,ai,eps,png,jpeg,etc)
• - Style sheet
Should not have
• - Text in images

```html
<!DOCTYPE html>
<html lang="en">
<head>
<meta charset="utf-8">
<title>Wrenfield — Apps for Zulmax</title>
<link rel="stylesheet" href="https://fonts.googleapis.com/css2?family=Arimo:wght@400;700&display=swap">
<style>
  :root {
    --page: #ffffff;
    --ink: #555555;
    --heading: #666666;
    --panel: #333333;
    --brand-red: #c8161e;
    --red-top: #d4141f;
    --red-bottom: #7e0710;
    --nav-top: #7a7a7a;
    --nav-bottom: #3b3b3b;
    --nav-active: #4a4a4a;
    --nav-divider: #2f2f2f;
    --footer: #3a3a3c;
    --footer-edge: #1f1f21;
    --white: #ffffff;
    --muted-light: #cfcfcf;
    --visual-light: #b9c6cb;
    --visual-dark: #4a5558;
  }
  * { box-sizing: border-box; margin: 0; padding: 0; }
  html, body { width: 1200px; height: 1170px; overflow: hidden; }
  body {
    position: relative;
    background: var(--page);
    font-family: "Arimo", Arial, sans-serif;
    color: var(--ink);
  }
  .abs { position: absolute; }

  /* Brand */
  .brand {
    display: flex; align-items: center; gap: 10px;
    font-size: 40px; font-weight: 400; color: var(--brand-red);
    letter-spacing: -0.5px; line-height: 1;
  }
  .brand-dot { width: 16px; height: 16px; border-radius: 50%; background: var(--brand-red); }
  .site-brand { left: 134px; top: 33px; }

  /* Navigation */
  .main-nav {
    left: 490px; top: 30px; width: 580px; height: 50px;
    border-radius: 6px; overflow: hidden;
    background: linear-gradient(var(--nav-top), var(--nav-bottom));
    border: 1px solid #2a2a2a;
    display: flex;
    box-shadow: inset 0 1px 0 rgba(255,255,255,.35);
  }
  .main-nav a {
    display: flex; align-items: center; justify-content: center; gap: 6px;
    color: var(--white); text-decoration: none; font-size: 15px;
    border-right: 1px solid var(--nav-divider);
    box-shadow: 1px 0 0 rgba(255,255,255,.15);
    text-shadow: 0 1px 1px rgba(0,0,0,.6);
  }
  .main-nav a:last-child { border-right: 0; box-shadow: none; }
  .main-nav a.is-active { background: linear-gradient(#3a3a3a, var(--nav-active)); color: #dddddd; }
  .candy { width: 10px; height: 10px; border-radius: 50%; background: var(--brand-red); display: inline-block; }

  /* Hero */
  .hero-panel {
    left: 130px; top: 120px; width: 940px; height: 380px;
    background: var(--panel); border-radius: 6px;
    box-shadow: 0 2px 3px rgba(0,0,0,.35);
  }
  .hero-visual {
    left: 200px; top: 150px; width: 325px; height: 510px;
    border-radius: 10px;
    background: linear-gradient(160deg, #1c1c1c, var(--visual-dark) 45%, var(--visual-light) 100%);
  }
  .tagline {
    left: 612px; top: 196px; width: 440px;
    font-size: 50px; line-height: 50px; letter-spacing: -3px;
    color: var(--white); font-weight: 400;
    text-shadow: 0 2px 3px rgba(0,0,0,.5);
  }
  .hero-copy {
    left: 611px; top: 325px; width: 350px;
    font-size: 16px; line-height: 20px; color: var(--white);
  }
  .cta-primary {
    left: 608px; top: 461px; width: 236px; height: 62px;
    border-radius: 7px; border: 1px solid #5e040a;
    background: linear-gradient(var(--red-top), var(--red-bottom));
    box-shadow: 0 2px 4px rgba(0,0,0,.45), inset 0 1px 0 rgba(255,255,255,.3);
    color: var(--white); font-size: 22px; letter-spacing: -0.5px;
    display: flex; align-items: center; justify-content: center; gap: 12px;
    text-decoration: none;
  }
  .cta-primary .dot { width: 11px; height: 11px; border-radius: 50%; background: #f2b3b6; }
  .secondary-copy {
    left: 611px; top: 588px; width: 210px;
    font-size: 11px; line-height: 15px; color: var(--ink);
  }
  .cta-secondary {
    left: 849px; top: 588px; width: 161px; height: 43px;
    border-radius: 4px; border: 1px solid #3a3a3a;
    background: linear-gradient(#8a8a8a, #4a4a4a);
    color: var(--white); font-size: 12px; text-decoration: none;
    display: flex; align-items: center; justify-content: center;
    box-shadow: inset 0 1px 0 rgba(255,255,255,.3);
  }

  /* Products */
  .section-title { left: 130px; top: 710px; font-size: 22px; color: var(--heading); font-weight: 400; letter-spacing: -0.8px; }
  .product-shot {
    width: 220px; height: 150px;
    background: linear-gradient(160deg, #2a2a2a, #7c979f 40%, var(--visual-light));
  }
  .product-shot.one { left: 130px; top: 760px; }
  .product-shot.two { left: 610px; top: 760px; }
  .offer-tag {
    left: 127px; top: 770px; width: 72px; height: 20px;
    background: #8e0b12; color: var(--white);
    font-size: 11px; font-weight: 700; letter-spacing: -0.3px;
    display: flex; align-items: center; padding-left: 9px;
    clip-path: polygon(0 0, 100% 0, 90% 100%, 0 100%);
  }
  .product-copy { width: 212px; font-size: 11px; line-height: 15px; color: var(--ink); }
  .product-copy.one { left: 371px; top: 760px; }
  .product-copy.two { left: 852px; top: 760px; }
  .store-badge {
    width: 163px; height: 59px; border-radius: 6px;
    background: linear-gradient(var(--red-top), var(--red-bottom));
    border: 1px solid #5e040a;
    box-shadow: 0 1px 3px rgba(0,0,0,.35), inset 0 1px 0 rgba(255,255,255,.3);
    color: var(--white); text-decoration: none;
    display: flex; align-items: center; padding-left: 12px; gap: 9px;
  }
  .store-badge svg { flex: none; }
  .store-label { display: flex; flex-direction: column; line-height: 1; }
  .store-small { font-size: 13px; letter-spacing: 0.6px; }
  .store-large { font-size: 22px; letter-spacing: -0.5px; margin-top: 2px; }
  .store-badge.one { left: 369px; top: 849px; }
  .store-badge.two { left: 849px; top: 849px; }

  /* Footer */
  .site-footer {
    left: 0; top: 1000px; width: 1200px; height: 170px;
    background: var(--footer); border-top: 3px solid var(--footer-edge);
  }
  .copyright { left: 136px; top: 1030px; font-size: 11px; color: var(--muted-light); }
  .footer-brand { left: 134px; top: 1055px; }
  .footer-nav { left: 490px; top: 1064px; width: 580px; height: 20px; display: flex; }
  .footer-nav a {
    display: flex; align-items: center; justify-content: center; gap: 6px;
    color: var(--white); text-decoration: none; font-size: 15px;
    text-shadow: 0 1px 1px rgba(0,0,0,.6);
  }
</style>
</head>
<body>

<header>
  <div class="abs brand site-brand"><span class="brand-dot"></span>Wrenfield</div>
  <nav class="abs main-nav">
    <a href="#" class="is-active" style="width:93px">Home</a>
    <a href="#" style="width:103px"><span class="candy"></span>Apps</a>
    <a href="#" style="width:97px">Support</a>
    <a href="#" style="width:90px">Blog</a>
    <a href="#" style="width:100px">Contact</a>
    <a href="#" style="width:97px">About</a>
  </nav>
</header>

<main>
  <section class="abs hero-panel"></section>
  <div class="abs hero-visual" role="img" aria-label="Product photo: front and side view of a Zulmax phone showing its home screen"></div>
  <h1 class="abs tagline">This is a nice<br>and short tagline.</h1>
  <p class="abs hero-copy">And this is some dummy text: but as the junior mates were hurrying to execute the order, a pale man, with a bandaged head, arrested them.</p>
  <a href="#" class="abs cta-primary"><span class="dot"></span>Call to Action<span class="dot"></span></a>
  <p class="abs secondary-copy">And this is some dummy text: dorothy did not say anything, for she was puzzled to know which of her two friends was right.</p>
  <a href="#" class="abs cta-secondary">Secondary Action</a>

  <h2 class="abs section-title">Our Products</h2>

  <div class="abs product-shot one" role="img" aria-label="Product photo: Zulmax phone screen with app icons"></div>
  <div class="abs offer-tag">20% OFF</div>
  <p class="abs product-copy one">This is some dummy text: beyond the DUODECIMO, this system does not proceed, inasmuch as the Porpoise is the smallest of the whales. Above, you have all the Leviathans of note.</p>
  <a href="#" class="abs store-badge one">
    <svg width="18" height="32" viewBox="0 0 18 32" aria-hidden="true"><rect x="1.5" y="1.5" width="15" height="29" rx="3" fill="none" stroke="#fff" stroke-width="2.5"/><rect x="4" y="6" width="10" height="18" fill="#fff"/></svg>
    <span class="store-label"><span class="store-small">Available on the</span><span class="store-large">App Market</span></span>
  </a>

  <div class="abs product-shot two" role="img" aria-label="Product photo: Zulmax phone screen with app icons"></div>
  <p class="abs product-copy two">This is some dummy text: but there are a rabble of uncertain, fugitive, half-fabulous whales, which, as an American whaleman, I know by reputation, but not personally.</p>
  <a href="#" class="abs store-badge two">
    <svg width="18" height="32" viewBox="0 0 18 32" aria-hidden="true"><rect x="1.5" y="1.5" width="15" height="29" rx="3" fill="none" stroke="#fff" stroke-width="2.5"/><rect x="4" y="6" width="10" height="18" fill="#fff"/></svg>
    <span class="store-label"><span class="store-small">Available on the</span><span class="store-large">App Market</span></span>
  </a>
</main>

<footer>
  <div class="abs site-footer"></div>
  <p class="abs copyright">©2010 Wrenfield. All Rights Reserved.</p>
  <div class="abs brand footer-brand"><span class="brand-dot"></span>Wrenfield</div>
  <nav class="abs footer-nav">
    <a href="#" style="width:93px">Home</a>
    <a href="#" style="width:103px"><span class="candy"></span>Apps</a>
    <a href="#" style="width:97px">Support</a>
    <a href="#" style="width:90px">Blog</a>
    <a href="#" style="width:100px">Contact</a>
    <a href="#" style="width:97px">About</a>
  </nav>
</footer>

</body>
</html>
```